Tactical Supply Company needing memorable business card design

Our tactical supply comapny is in need of a new business card design that will set us apart from the amateurs. We sell tactical gear ranging from backpacks and range bags to apparel and other gear. We are looking for a sharp design that incorporates our logo, website, and name. Our colors are white, red, and black, or any combination of the three, preferably red and black.
I have attached our logo with our name underneath but I have also edited that design with the logo incorporated next to the name (attached).

Target Market(s)

Law enforcement, military, tactical

Industry/Entity Type

Business

Contact Information for Business Card

Include www.brindlequarry.example

Colors
000000
ec1f27
ffffff

Requirements
Must have
• Our name, logo, and website. This is intended to be a memorable simple card, no name, address, email, or phone number info is necessary. Designs that do include this additional info will still be considered if they are absolutely spectacular.
Should not have
• A standard template design, I can create that in my own on Cardomix. I am looking for a new, creative design that is completely unique to my company.

```html
<!DOCTYPE html>
<html lang="en">
<head>
<meta charset="utf-8">
<title>Brindle Quarry – Business Card</title>
<link href="https://fonts.googleapis.com/css2?family=Source+Sans+3:wght@400;600;700&display=swap" rel="stylesheet">
<style>
  :root {
    --black: #231f20;
    --red: #ec1f27;
    --white: #ffffff;
    --backdrop: #ecebe8;
    --edge: #6d6d6d;
  }
  * { box-sizing: border-box; margin: 0; padding: 0; }
  html, body {
    width: 1168px; height: 1200px; overflow: hidden;
    background: var(--backdrop);
    font-family: "Source Sans 3", Arial, sans-serif;
    color: var(--black);
  }
  .canvas { position: relative; width: 1168px; height: 1200px; }
  .card {
    position: absolute;
    background: var(--white);
    border: 1px solid var(--edge);
    overflow: hidden;
  }
  .card--front { left: 229px; top: 53px; width: 890px; height: 510px; }
  .card--back  { left: 43px;  top: 635px; width: 888px; height: 509px; }

  .name-tab {
    position: absolute; left: 0; top: 74px;
    width: 25px; height: 78px;
    background: var(--black);
    border-radius: 0 14px 14px 0;
  }
  .holder-name {
    position: absolute; left: 42px; top: 76px;
    font-size: 33px; font-weight: 700; line-height: 1;
  }
  .holder-title {
    position: absolute; left: 42px; top: 116px;
    font-size: 26px; font-weight: 700; color: var(--red);
    letter-spacing: 0.5px; line-height: 1;
  }
  .contact-list {
    position: absolute; left: 40px; top: 296px;
    list-style: none; font-size: 23px; line-height: 34px;
  }
  .contact-list li { display: flex; align-items: center; gap: 8px; }
  .contact-list svg { width: 20px; height: 20px; flex: none; }
  .address {
    position: absolute; left: 41px; top: 406px;
    font-size: 23px; line-height: 30px; font-style: normal;
  }
  .web-pill {
    position: absolute; left: 466px; top: 470px;
    width: 380px; height: 42px;
    background: var(--black); color: var(--white);
    border-radius: 22px 22px 0 0;
    display: flex; align-items: center; justify-content: center;
    font-size: 22px; letter-spacing: 2px;
  }
  .brand {
    position: absolute;
    display: flex; align-items: center; gap: 14px;
    font-weight: 700; color: var(--black);
    text-transform: uppercase; line-height: 1;
  }
  .brand-square { background: var(--red); flex: none; }
  .card--front .brand { left: 470px; top: 136px; font-size: 42px; letter-spacing: 1px; }
  .card--front .brand-square { width: 34px; height: 34px; }
  .card--back .brand {
    left: 0; right: 0; top: 200px; justify-content: center;
    font-size: 64px; letter-spacing: 2px;
  }
  .card--back .brand-square { width: 52px; height: 52px; }
  .back-web {
    position: absolute; left: 0; right: 0; top: 430px;
    text-align: center; font-size: 31px; letter-spacing: 6px;
  }
</style>
</head>
<body>
<div class="canvas">

  <section class="card card--front">
    <div class="name-tab"></div>
    <h1 class="holder-name">Your Name</h1>
    <p class="holder-title">Title</p>

    <div class="brand"><span class="brand-square"></span>Brindle Quarry</div>

    <ul class="contact-list">
      <li>
        <svg viewBox="0 0 20 20" aria-hidden="true"><circle cx="10" cy="10" r="9" fill="none" stroke="var(--red)" stroke-width="2"/><path d="M7 5c-1 1-1 3 1 6s4 4 5 3l1-1-2-2-1 1c-1-1-2-2-2-3l1-1-2-2z" fill="var(--red)"/></svg>
        012-345-6789
      </li>
      <li>
        <svg viewBox="0 0 20 20" aria-hidden="true"><path d="M3 11l2-5h10l2 5v5h-3v-2H6v2H3z" fill="var(--red)"/><circle cx="6" cy="12" r="1.3" fill="#fff"/><circle cx="14" cy="12" r="1.3" fill="#fff"/></svg>
        012-345-6789
      </li>
      <li>
        <svg viewBox="0 0 20 20" aria-hidden="true"><rect x="2" y="5" width="16" height="11" rx="1.5" fill="var(--red)"/><path d="M2.5 6l7.5 5 7.5-5" fill="none" stroke="#fff" stroke-width="1.6"/></svg>
        info@brindlequarry.example
      </li>
    </ul>

    <address class="address">Street Name, City Name<br>Zipcode-01234</address>

    <div class="web-pill">www.brindlequarry.example</div>
  </section>

  <section class="card card--back">
    <div class="brand"><span class="brand-square"></span>Brindle Quarry</div>
    <p class="back-web">www.brindlequarry.example</p>
  </section>

</div>
</body>
</html>
```